Bolt Ridge Hoist Service Business Cards

I need a business card for "Bolt Ridge Hoist and Tackle"

Boltridge2023@hoistmail.example

Hoist Works LLC, Bolt Ridge Hoist and Tackle LLC

555.204.7186 | www.BOLTRIDGEHOISTS.example

Central Indiana & Northeast Ohio

(IN) 23810 Meadow Lane Noblesville, IN 46099

(OH) 4150 Dunmore Street Akron, Ohio 44397

Contact Information for Business Card

Colors
0094D4
00A9DD
6FCCEA
C7EBF8
E9F6FB
59FF00
82FF00
B8FF75
E3FFCB
F4FFEA
EE7325
F08F49
F5BC92
FAE3D3
FDF4ED
EB3D1F
EC4F4E
F09395
F8D3D4
FCEDEE
E54698
E96AAD
F1A4CE
F9D9EA
FCEFF6
A7469A
B969AE
D3A5CF
EDDBEB
F8F0F9

```html
<!DOCTYPE html>
<html lang="en">
<head>
<meta charset="utf-8">
<title>Bolt Ridge Hoist Service Business Cards</title>
<link rel="stylesheet" href="https://fonts.googleapis.com/css2?family=Archivo+Black&family=Open+Sans:wght@400;700&display=swap">
<style>
  :root {
    --stage: #1d1d1d;
    --card: #030303;
    --green: #22cc3c;
    --red: #eb3d1f;
    --white: #ffffff;
  }
  * { box-sizing: border-box; margin: 0; padding: 0; }
  html, body { width: 1200px; height: 1015px; overflow: hidden; background: var(--stage); }
  .card {
    position: absolute; left: 250px; width: 700px; height: 400px;
    background: var(--card); overflow: hidden;
  }
  .card-front { top: 60px; }
  .card-back { top: 545px; }

  /* front */
  .front-scene {
    position: absolute; left: 380px; top: 20px; width: 300px; height: 320px;
    background: linear-gradient(160deg, #3a3a3a 0%, #5c5c5c 35%, #8a3222 60%, #1f8a32 100%);
    border-radius: 4px;
  }
  .front-brand {
    position: absolute; left: 40px; top: 220px; width: 320px;
    display: flex; align-items: flex-start; gap: 12px;
  }
  .brand-mark { width: 16px; height: 16px; background: var(--green); margin-top: 10px; flex: none; }
  .front-brand .brand-name {
    font-family: "Archivo Black", sans-serif; color: var(--white);
    font-size: 32px; line-height: 1.08; letter-spacing: 1px;
  }

  /* back */
  .wave { position: absolute; left: 0; top: 0; width: 700px; height: 400px; }
  .back-contact {
    position: absolute; right: 36px; top: 22px; text-align: right;
  }
  .company-llc {
    font-family: "Archivo Black", sans-serif; color: var(--green);
    font-size: 21px; letter-spacing: 1px;
  }
  .company-name {
    font-family: "Archivo Black", sans-serif; color: var(--white);
    font-size: 19px; line-height: 1.15; letter-spacing: 1px; margin-top: 2px;
  }
  .contact-list { list-style: none; margin-top: 8px; }
  .contact-list li {
    font-family: "Open Sans", sans-serif; color: var(--white); font-size: 15px;
    line-height: 22px; display: flex; justify-content: flex-end; align-items: center; gap: 8px;
  }
  .contact-list svg { width: 15px; height: 15px; }
  .back-logo {
    position: absolute; left: 36px; top: 100px; width: 260px;
  }
  .back-logo .crane-art {
    width: 240px; height: 90px;
    background: linear-gradient(90deg, #d9d9d9 0%, #9a9a9a 50%, #22cc3c 100%);
    border-radius: 4px;
  }
  .back-logo .brand-name {
    font-family: "Archivo Black", sans-serif; color: var(--green);
    font-size: 17px; line-height: 1.15; margin-top: 8px; letter-spacing: 1px;
  }
  .back-address {
    position: absolute; right: 28px; bottom: 22px; text-align: right;
    font-family: "Open Sans", sans-serif; color: var(--white);
  }
  .region { font-weight: 700; font-size: 18px; margin-bottom: 2px; }
  .address { font-size: 15px; line-height: 1.5; }
</style>
</head>
<body>
  <section class="card card-front">
    <div class="front-scene" role="img" aria-label="Illustration of a boom truck and a mobile crane in front of a grey city skyline"></div>
    <div class="front-brand">
      <span class="brand-mark"></span>
      <div class="brand-name">BOLT RIDGE<br>HOIST AND<br>TACKLE</div>
    </div>
  </section>

  <section class="card card-back">
    <svg class="wave" viewBox="0 0 700 400" aria-hidden="true">
      <path d="M0,330 C230,335 380,230 700,200 L700,209 C384,240 234,345 0,340 Z" fill="var(--red)"/>
      <path d="M0,350 C230,355 380,250 700,220 L700,400 L0,400 Z" fill="var(--green)"/>
      <path d="M0,358 C232,363 383,259 700,229 L700,233 C385,264 234,368 0,363 Z" fill="var(--card)"/>
    </svg>
    <div class="back-logo">
      <div class="crane-art" role="img" aria-label="Line drawing of a mobile crane with extended boom"></div>
      <div class="brand-name">BOLT RIDGE HOIST<br>AND TACKLE</div>
    </div>
    <div class="back-contact">
      <div class="company-llc">HOIST WORKS LLC</div>
      <div class="company-name">BOLT RIDGE HOIST AND<br>TACKLE LLC</div>
      <ul class="contact-list">
        <li>555.204.7186
          <svg viewBox="0 0 16 16"><path d="M4 1l3 3-2 2c1 2 3 4 5 5l2-2 3 3-2 3C7 15 1 9 1 3z" fill="var(--green)"/></svg></li>
        <li>Boltridge2023@hoistmail.example
          <svg viewBox="0 0 16 16"><rect x="1" y="3" width="14" height="10" fill="var(--green)"/><path d="M1 3l7 6 7-6" stroke="var(--card)" stroke-width="1.4" fill="none"/></svg></li>
        <li>www.BOLTRIDGEHOISTS.example
          <svg viewBox="0 0 16 16"><circle cx="8" cy="8" r="6.5" stroke="var(--green)" stroke-width="1.5" fill="none"/><path d="M1.5 8h13M8 1.5c-3 3-3 10 0 13M8 1.5c3 3 3 10 0 13" stroke="var(--green)" stroke-width="1.2" fill="none"/></svg></li>
      </ul>
    </div>
    <div class="back-address">
      <div class="region">Central Indiana &amp; Northeast Ohio</div>
      <div class="address">(IN) 23810 Meadow Lane Noblesville, IN 46099</div>
      <div class="address">(OH) 4150 Dunmore Street Akron, Ohio 44397</div>
    </div>
  </section>
</body>
</html>
```